Letter Head, for use on daily correspondence with other companies

Hi

I want a professional Letter head, That my company can use to corresponded with other companies we do business with on a daily basis.

I want this done as soon as possible as this is peak session for us.

I have attached the company logo so please be creative and professional.
Kind regards

Osric

Target Market(s)

All Audience searching for tickets, people in the entertainment world

Industry/Entity Type

Entertainment Industry

Font styles to use
Serif
Sans Serif
Decorative
Script

Requirements
Must have
• Very professional image.
• I will know want i want when i see it
• so please do your utmost in your professional standards
• Address of the company 47 marlow lane, telephone number 0207 581 2937
• Vat number: 486 2917 58.
• This letter head my be able to acomodate usage for directors & CEO as well as managers and employess
Nice to have
• A great professional image
Should not have
• Be creative please

```html
<!DOCTYPE html>
<html lang="en">
<head>
<meta charset="utf-8">
<title>Stagepass Letterhead</title>
<link href="https://fonts.googleapis.com/css2?family=Noto+Serif:wght@400;700&display=swap" rel="stylesheet">
<style>
  :root {
    --brand-red: #e4252f;
    --ink: #5b5b5b;
    --paper: #ffffff;
  }
  html, body {
    margin: 0;
    padding: 0;
    overflow: hidden;
    background: var(--paper);
  }
  .letterhead {
    position: relative;
    width: 927px;
    height: 1200px;
    background: var(--paper);
    overflow: hidden;
    font-family: "Noto Serif", Georgia, serif;
    color: var(--ink);
  }
  .brand-block {
    position: absolute;
    left: 0;
    top: 46px;
    width: 228px;
    height: 107px;
    background: var(--brand-red);
    display: flex;
    align-items: center;
    justify-content: flex-end;
    padding-right: 22px;
    box-sizing: border-box;
  }
  .brand-name {
    color: var(--paper);
    font-weight: 700;
    font-size: 24px;
    letter-spacing: 0.5px;
  }
  .edge-mark {
    position: absolute;
    right: 0;
    top: 46px;
    width: 8px;
    height: 107px;
    background: var(--brand-red);
  }
  .address, .company-details {
    position: absolute;
    top: 80px;
    font-size: 13.6px;
    line-height: 18px;
    letter-spacing: 0.6px;
  }
  .address { left: 287px; }
  .company-details { right: 80px; text-align: right; }
  .address .street, .company-details strong { font-weight: 700; }
  .footer-band {
    position: absolute;
    left: 0;
    bottom: 0;
    width: 100%;
    height: 15px;
    background: var(--brand-red);
  }
</style>
</head>
<body>
  <div class="letterhead">
    <header>
      <div class="brand-block"><span class="brand-name">Stagepass</span></div>
      <div class="address">
        <div class="street">47 Marlow Lane,</div>
        <div>London, United Kingdom</div>
      </div>
      <div class="company-details">
        <div>Vat No. <strong>486.2917.58</strong></div>
        <div><strong>T: 0207.581.2937</strong></div>
      </div>
      <div class="edge-mark"></div>
    </header>
    <footer class="footer-band"></footer>
  </div>
</body>
</html>
```